Velvet Basin Suites, a portable luxury restroom trailer company needs a landing page

We need a landing page for a luxury portable restroom trailer company. This should be modern, and simple - use any combination of Pantone colors: Warm Gray 1C, Black 7C, 7529c, 873C, 8003C

We rent these trailers for special events like weddings, private parties, festivals, family reunions, team building, wine tastings, beer tastings, food truck round-ups, etc.

An idea of the landing page is in the files below. Please use stock photography and placeholder text for now. The winning design will be given final content.

Requirements
Must have
• Multiple "Get Quote" buttons or a place for them to type in type of rental, how many people etc

```html
<!DOCTYPE html>
<html lang="en">
<head>
<meta charset="utf-8">
<title>Velvet Basin Suites — Luxury Restroom Trailers</title>
<link rel="stylesheet" href="https://fonts.googleapis.com/css2?family=Playfair+Display:wght@400;500&family=Lora:wght@400&display=swap">
<style>
:root{
  --warm-gray:#f3ece8;
  --gold:#c29f63;
  --brown:#6c4d38;
  --slate:#4f5e88;
  --slate-dark:#4a5a7e;
  --stone:#9ea2aa;
  --ink:#3a3a44;
  --muted:#8a8a92;
  --white:#ffffff;
  --serif:"Playfair Display", Georgia, serif;
  --body:"Lora", Georgia, serif;
}
*{box-sizing:border-box;margin:0;padding:0}
html,body{width:1200px;height:4835px;overflow:hidden}
body{font-family:var(--body);color:var(--ink);background:var(--white)}
section,header,footer,nav{position:relative;width:1200px;overflow:hidden}
.abs{position:absolute}
.eyebrow{font-family:var(--serif);font-size:9px;letter-spacing:3px;text-transform:uppercase}
.title{font-family:var(--serif);font-weight:400;font-size:24px;line-height:32px}
.rule{width:22px;height:1px;margin:14px 0}
.copy{font-size:9px;line-height:15px}
.cta{display:flex;align-items:center;gap:12px;font-size:9px;margin-top:18px;text-decoration:none;color:inherit}
.cta svg{width:38px;height:8px}

/* hero */
.hero{height:613px;color:var(--white);text-align:center}
.hero-photo{position:absolute;inset:0;background:
  linear-gradient(180deg,rgba(60,45,35,.35),rgba(60,45,35,.55)),
  linear-gradient(180deg,#b7a597 0%,#a8978a 35%,#7d7a5a 60%,#8c8b6a 80%,#a69c86 100%)}
.topbar{position:absolute;top:30px;left:240px;right:240px;display:flex;justify-content:space-between;align-items:center}
.brand-small{font-family:var(--serif);font-size:10px;letter-spacing:3px;text-transform:uppercase}
.hero-mark{position:absolute;top:190px;left:0;right:0;display:flex;flex-direction:column;align-items:center;gap:8px}
.hero-mark .dot{width:30px;height:30px;border:1px solid rgba(255,255,255,.8);border-radius:50%}
.hero-mark span{font-family:var(--serif);font-size:14px;letter-spacing:1px}
.hero .since{position:absolute;top:305px;left:0;right:0;font-size:10px;letter-spacing:4px}
.hero h1{position:absolute;top:345px;left:0;right:0;font-family:var(--serif);font-weight:400;font-size:25px;letter-spacing:7px}
.hero .sub{position:absolute;top:400px;left:0;right:0;font-size:9px;letter-spacing:4px}

/* nav strip */
.quicklinks{height:95px;background:var(--warm-gray)}
.quicklink{position:absolute;top:28px;font-family:var(--serif);font-size:18px;color:var(--ink)}
.quicklink .eyebrow{display:block;font-size:7px;margin-bottom:4px;color:var(--muted)}

/* photo features */
.feature{height:508px;color:var(--white)}
.feature-photo{position:absolute;inset:0}
.feature-gold .feature-photo{background:linear-gradient(90deg,var(--gold) 0%,var(--gold) 22%,rgba(194,159,99,.6) 38%,rgba(150,120,90,0) 55%),
  linear-gradient(90deg,#9d8063,#c9b08d 45%,#e2cdb4 60%,#3a2b25 85%,#5a4a30 100%)}
.feature-brown .feature-photo{background:linear-gradient(90deg,var(--brown) 0%,var(--brown) 16%,rgba(108,77,56,.5) 28%,rgba(108,77,56,0) 42%),
  linear-gradient(90deg,#7e5f4a,#c7b4a6 40%,#e7ddd3 65%,#d8c8b9 100%)}
.feature-text{position:absolute;top:88px;width:200px}

/* split sections */
.split{height:415px}
.split-blue{background:var(--slate);color:var(--white)}
.split-white{background:var(--white);color:var(--slate);height:413px}
.photo-box{position:absolute;box-shadow:0 6px 14px rgba(0,0,0,.18)}
.split-text{position:absolute;width:300px}
.split-white .copy{color:var(--muted)}
.split-white .cta{color:var(--ink)}

/* testimonial */
.testimonial{height:331px;background:var(--stone);color:var(--white);text-align:center}
.testimonial blockquote{position:absolute;top:128px;left:0;right:0;font-family:var(--serif);font-size:17px;line-height:25px}
.testimonial cite{position:absolute;top:196px;left:0;right:0;font-style:normal;font-size:8px;letter-spacing:3px}

/* blush rows */
.blush{height:827px;background:linear-gradient(180deg,#f1ebe8 0%,#dcc6c4 35%,#e4d3d1 65%,#f6f2f1 100%);color:var(--slate)}
.blush .copy{color:var(--muted)}
.blush .cta{color:var(--ink)}

/* mission */
.mission{height:918px;background:linear-gradient(180deg,#c9c9cf 0%,#e4e4e8 30%,#f5f5f7 60%,#ffffff 100%);text-align:center;color:var(--slate)}
.mission .giant{position:absolute;top:80px;left:0;right:0;font-family:var(--serif);font-size:78px;letter-spacing:36px;color:rgba(79,94,136,.18)}
.mission h2{position:absolute;top:140px;left:0;right:0;font-family:var(--serif);font-weight:400;font-size:22px;line-height:32px}
.video{position:absolute;left:240px;top:262px;width:720px;height:323px;border-radius:8px;background:linear-gradient(90deg,#2e3c5e,#6b7a99 35%,#2b3756 55%,#5d6d8e 80%,#2f3b5a)}
.play{position:absolute;left:50%;top:50%;width:44px;height:44px;margin:-22px 0 0 -22px;border-radius:50%;background:var(--white);display:flex;align-items:center;justify-content:center}
.contact{position:absolute;top:700px;left:0;right:0;display:flex;flex-direction:column;align-items:center}
.contact .eyebrow{font-size:8px;color:var(--muted)}
.contact h3{font-family:var(--serif);font-weight:400;font-size:22px;margin-top:10px}
.contact .copy{width:360px;color:var(--muted)}
.contact .cta{color:var(--slate)}

/* footer */
.site-footer{height:206px;background:var(--slate-dark);color:var(--white)}
.social{position:absolute;top:38px;left:240px;display:flex;gap:14px}
.social span{width:13px;height:13px;border-radius:50%;background:var(--white)}
.footer-nav{position:absolute;top:40px;right:240px;display:flex;gap:22px;font-size:8px;letter-spacing:1px;text-transform:uppercase}
.legal{position:absolute;top:150px;left:240px;font-size:7px}
.footer-brand{position:absolute;top:140px;right:240px;font-family:var(--serif);font-size:12px}
</style>
</head>
<body>

<header class="hero">
  <div class="hero-photo" role="img" aria-label="Outdoor garden event at a villa with a stage and rattan chairs"></div>
  <div class="topbar">
    <svg width="14" height="10" viewBox="0 0 14 10" fill="none" stroke="#fff" stroke-width="1"><path d="M0 1h14M0 5h14M0 9h14"/></svg>
    <span class="brand-small">Velvet Basin Suites</span>
    <svg width="11" height="11" viewBox="0 0 12 12" fill="none" stroke="#fff" stroke-width="1"><circle cx="5" cy="5" r="4"/><path d="M8 8l3.5 3.5"/></svg>
  </div>
  <div class="hero-mark"><div class="dot"></div><span>Velvet Basin Suites</span></div>
  <p class="since">LUXURY EVENTS SINCE 2017</p>
  <h1>THE ART OF LUXURY RESTROOM</h1>
  <p class="sub">FOR A MAGNIFICENT EVENT</p>
</header>

<nav class="quicklinks">
  <a class="quicklink" style="left:240px"><span class="eyebrow">Lorem</span>Luxury Events</a>
  <a class="quicklink" style="left:532px"><span class="eyebrow">Lorem</span>Royal Products</a>
  <a class="quicklink" style="right:240px;text-align:right"><span class="eyebrow">Lorem</span>Contact Us</a>
</nav>

<section class="feature feature-gold">
  <div class="feature-photo" role="img" aria-label="Guests toasting with champagne at a festive dinner table"></div>
  <div class="feature-text" style="left:240px">
    <p class="eyebrow">Lorem Ipsum</p>
    <h2 class="title" style="margin-top:14px">Lorem Ipsum<br>Dolor Sit Amet<br>Consectetur</h2>
    <div class="rule" style="background:rgba(255,255,255,.6)"></div>
    <p class="copy">Elegant restroom trailers for weddings, galas and private parties. Fresh linens, soft lighting and attentive service make every visit feel effortless for your guests.</p>
    <a class="cta">Get A Quote Today <svg viewBox="0 0 38 8" fill="none" stroke="currentColor"><path d="M0 4h37M33 1l4 3-4 3"/></svg></a>
  </div>
</section>

<section class="feature feature-brown">
  <div class="feature-photo" role="img" aria-label="Red wine being poured into glasses on a set table"></div>
  <div class="feature-text" style="left:708px">
    <p class="eyebrow">Lorem Ipsum</p>
    <h2 class="title" style="margin-top:14px">Lorem Ipsum<br>Dolor Sit Amet<br>Consectetur</h2>
    <div class="rule" style="background:rgba(255,255,255,.6)"></div>
    <p class="copy">From vineyard tastings to garden receptions, our suites arrive spotless, climate controlled and styled to sit quietly beside the finest tables of the evening.</p>
    <a class="cta">Contact Us Now <svg viewBox="0 0 38 8" fill="none" stroke="currentColor"><path d="M0 4h37M33 1l4 3-4 3"/></svg></a>
  </div>
</section>

<section class="split split-blue">
  <div class="photo-box" style="left:240px;top:95px;width:195px;height:274px;background:linear-gradient(160deg,#e9e9ec,#9a9ca3 60%,#c9a36f)" role="img" aria-label="Restroom trailer on wheels with open side"></div>
  <div class="photo-box" style="left:400px;top:95px;width:172px;height:225px;background:linear-gradient(180deg,#d8d8da,#8e8f94)" role="img" aria-label="Trailer interior with grey stalls and lighting"></div>
  <div class="split-text" style="left:625px;top:102px">
    <p class="eyebrow">Lorem Ipsum</p>
    <h2 class="title" style="margin-top:14px">Lorem Ipsum Dolor Sit<br>Amet Consectetur</h2>
    <div class="rule" style="background:rgba(255,255,255,.6)"></div>
    <p class="copy">Each trailer features porcelain fixtures, vanity mirrors, running water and music, delivered and serviced by a dedicated attendant for the length of your event.</p>
    <a class="cta">Get A Quote Today <svg viewBox="0 0 38 8" fill="none" stroke="currentColor"><path d="M0 4h37M33 1l4 3-4 3"/></svg></a>
  </div>
</section>

<section class="split split-white">
  <div class="split-text" style="left:240px;top:102px">
    <p class="eyebrow" style="color:var(--muted)">Lorem Ipsum</p>
    <h2 class="title" style="margin-top:14px">Lorem Ipsum Dolor Sit<br>Amet Consectetur</h2>
    <div class="rule" style="background:var(--slate)"></div>
    <p class="copy">Choose from two, four or eight station units with private stalls, polished finishes and accessible ramps to suit reunions, festivals and corporate retreats.</p>
    <a class="cta">Contact Us Now <svg viewBox="0 0 38 8" fill="none" stroke="currentColor"><path d="M0 4h37M33 1l4 3-4 3"/></svg></a>
  </div>
  <div class="photo-box" style="left:625px;top:91px;width:335px;height:228px;background:linear-gradient(180deg,#9fb2c8,#b9b9bb 45%,#6e7467)" role="img" aria-label="Silver restroom trailer parked outdoors"></div>
  <div class="photo-box" style="left:625px;top:230px;width:195px;height:139px;background:linear-gradient(180deg,#cfcfd1,#8f9095)" role="img" aria-label="Bright trailer interior hallway"></div>
</section>

<section class="testimonial">
  <blockquote>I would like to personally thank you for your outstanding<br>product. We've used Velvet Basin Suites for the last five years.</blockquote>
  <cite>MARIAN HOLLIS — SAVANNAH</cite>
</section>

<section class="blush">
  <div class="split-text" style="left:240px;top:100px">
    <p class="eyebrow" style="color:var(--muted)">Lorem Ipsum</p>
    <h2 class="title" style="margin-top:14px">Lorem Ipsum Dolor Sit<br>Amet Consectetur</h2>
    <div class="rule" style="background:var(--slate)"></div>
    <p class="copy">Tell us your date, venue and guest count and we will recommend the right suite, arrange delivery and handle setup before the first toast.</p>
    <a class="cta">Get A Free Quote Now <svg viewBox="0 0 38 8" fill="none" stroke="currentColor"><path d="M0 4h37M33 1l4 3-4 3"/></svg></a>
  </div>
  <div class="photo-box" style="left:625px;top:93px;width:335px;height:228px;background:linear-gradient(90deg,#8a7a68,#d8d2c8 50%,#b8aea0)" role="img" aria-label="Wine poured into glasses at a tasting"></div>

  <div class="split-text" style="left:240px;top:514px">
    <p class="eyebrow" style="color:var(--muted)">Lorem Ipsum</p>
    <h2 class="title" style="margin-top:14px">Lorem Ipsum Dolor Sit<br>Amet Consectetur</h2>
    <div class="rule" style="background:var(--slate)"></div>
    <p class="copy">Our team works with planners and caterers to place each trailer discreetly, keeping walkways clear and the atmosphere as refined as the occasion.</p>
    <a class="cta">Get A Free Quote Now <svg viewBox="0 0 38 8" fill="none" stroke="currentColor"><path d="M0 4h37M33 1l4 3-4 3"/></svg></a>
  </div>
  <div class="photo-box" style="left:625px;top:507px;width:335px;height:228px;background:linear-gradient(180deg,#c2c4a8,#8a8a82 50%,#2b2b30)" role="img" aria-label="Wedding couple beside a black car"></div>
</section>

<section class="mission">
  <p class="giant">OUR MISSION</p>
  <h2>Perfect Luxury Restroom<br>Especially For Your Event</h2>
  <div class="video" role="img" aria-label="Video of friends toasting with red wine">
    <div class="play"><svg width="10" height="12" viewBox="0 0 10 12"><path d="M1 0l9 6-9 6z" fill="#4f5e88"/></svg></div>
  </div>
  <div class="contact">
    <p class="eyebrow">Contact Us</p>
    <h3>Contact Us For A Quote</h3>
    <div class="rule" style="background:var(--slate)"></div>
    <p class="copy">Share the type of rental, number of guests and event date, and a coordinator will reply with a tailored quote within one business day.</p>
    <a class="cta">Get A Free Quote Now <svg viewBox="0 0 38 8" fill="none" stroke="currentColor"><path d="M0 4h37M33 1l4 3-4 3"/></svg></a>
  </div>
</section>

<footer class="site-footer">
  <div class="social"><span></span><span></span><span></span></div>
  <ul class="footer-nav" style="list-style:none"><li>Home</li><li>About Us</li><li>Contact Us</li><li>Our Products</li><li>Blog</li></ul>
  <p class="legal">© 2022 All Rights Reserved. Velvet Basin Suites.</p>
  <p class="footer-brand">Velvet Basin Suites</p>
</footer>

</body>
</html>
```